Kestrel Ledger Stationary
Business cards and MS Word letterhead template
Creative Brief
Use same font as used in my logo
Bank Gothic
Modern
Marcus Bellweather
Chief Operating Officer
4826 N Halvern RD, STE 212 Tempe, AZ 85291
marcus.bellweather@kestrelledger.example
www.kestrelledger.example
Stationary requirements: MS Word template with logo, address and phone in the header. Vector graphics Color and grayscale
Logo or other design element and the following text: "Kestrel Ledger, LLC is a registered ISO/MSP of Harwick Savings and Loan."

```html
<!DOCTYPE html>
<html lang="en">
<head>
<meta charset="utf-8">
<title>Kestrel Ledger Stationery</title>
<link href="https://fonts.googleapis.com/css2?family=Michroma&family=Roboto:wght@400;500&display=swap" rel="stylesheet">
<style>
:root{
  --board:#eadfcd;
  --paper:#ffffff;
  --blue:#3a64b0;
  --blue-soft:#e6ecf6;
  --grey:#8c8f94;
  --grey-dark:#5f6266;
  --ink:#3b3e44;
  --label:#4a3b2a;
}
*{margin:0;padding:0;box-sizing:border-box}
html,body{width:1200px;height:446px;overflow:hidden}
body{background:var(--board);position:relative;font-family:"Roboto",sans-serif;color:var(--ink)}
.label{position:absolute;font-family:"Michroma",sans-serif;font-size:6px;letter-spacing:.4px;color:var(--label);white-space:nowrap}
.piece{position:absolute;background:var(--paper);box-shadow:0 1px 3px rgba(0,0,0,.25);overflow:hidden}
.wave{position:absolute;left:0;bottom:0;width:100%}
.brand{display:flex;align-items:center;gap:4px;font-family:"Michroma",sans-serif;color:var(--blue);white-space:nowrap}
.brand-mark{background:var(--blue);flex:none}
.business-card{left:19px;width:101px;height:58px}
.business-card .brand{position:absolute;left:6px;top:8px;font-size:5px}
.business-card .brand-mark{width:8px;height:8px}
.card-person{position:absolute;left:7px;top:26px;font-size:3.4px;line-height:1.4}
.card-person b{font-weight:500;color:var(--blue)}
.card-back .brand{left:50%;top:50%;transform:translate(-50%,-50%);font-size:6px}
.letterhead{top:19px;width:276px;height:413px}
.letterhead .brand{position:absolute;left:18px;top:18px;font-size:8px}
.letterhead .brand-mark{width:12px;height:12px}
.letter-contact{position:absolute;font-size:3.6px;line-height:1.45;color:var(--grey-dark)}
.watermark{position:absolute;left:50%;top:140px;width:88px;height:88px;transform:translateX(-50%);background:var(--blue-soft);border-radius:6px}
.envelope{left:840px;width:348px}
.envelope .center-mark{position:absolute;left:50%;width:16px;height:16px;transform:translateX(-50%);background:var(--blue)}
.flap-line{position:absolute;inset:0;width:100%;height:100%}
.env-front .brand{position:absolute;left:12px;top:12px;font-size:7px}
.env-front .brand-mark{width:10px;height:10px}
.env-return{position:absolute;left:14px;top:50px;font-size:3.6px;line-height:1.45;color:var(--grey-dark)}
</style>
</head>
<body>

<p class="label" style="left:19px;top:190px">Business Cards</p>

<section class="piece business-card card-front" style="top:204px">
  <div class="brand"><span class="brand-mark"></span>KESTREL LEDGER</div>
  <div class="card-person"><b>Marcus Bellweather</b><br>Chief Operating Officer<br>4826 N Halvern RD, STE 212 Tempe, AZ 85291<br>marcus.bellweather@kestrelledger.example<br>www.kestrelledger.example</div>
  <svg class="wave" viewBox="0 0 101 14" preserveAspectRatio="none" height="14"><path d="M0 6 C30 0 55 14 101 4 L101 14 L0 14Z" fill="var(--blue)"/><path d="M0 4 C30 -2 55 12 101 2" stroke="var(--grey)" stroke-width=".8" fill="none"/></svg>
</section>
<p class="label" style="left:19px;top:268px">Business Card Front</p>

<section class="piece business-card card-back" style="top:283px">
  <div class="brand"><span class="brand-mark"></span>KESTREL LEDGER</div>
  <svg class="wave" viewBox="0 0 101 12" preserveAspectRatio="none" height="12"><path d="M0 6 C30 0 55 12 101 4 L101 12 L0 12Z" fill="var(--blue)"/></svg>
</section>
<p class="label" style="left:19px;top:347px">Business Card Back</p>

<section class="piece letterhead" style="left:168px">
  <div class="brand"><span class="brand-mark"></span>KESTREL LEDGER</div>
  <div class="letter-contact" style="right:16px;top:16px">4826 N Halvern RD, STE 212<br>Tempe, AZ 85291<br>Phone 480.555.0142<br>www.kestrelledger.example</div>
  <div class="watermark"></div>
  <svg class="wave" viewBox="0 0 276 70" preserveAspectRatio="none" height="70"><path d="M0 26 C70 4 150 50 276 14 L276 70 L0 70Z" fill="var(--blue)"/><path d="M0 20 C70 -2 150 44 276 8" stroke="var(--grey)" stroke-width="2" fill="none"/></svg>
</section>
<p class="label" style="left:268px;top:436px">Letterhead Option 1</p>

<section class="piece letterhead" style="left:475px">
  <div class="brand"><span class="brand-mark"></span>KESTREL LEDGER</div>
  <div class="watermark"></div>
  <div class="letter-contact" style="right:16px;bottom:74px">4826 N Halvern RD, STE 212<br>Tempe, AZ 85291<br>www.kestrelledger.example</div>
  <svg class="wave" viewBox="0 0 276 70" preserveAspectRatio="none" height="70"><path d="M0 26 C70 4 150 50 276 14 L276 70 L0 70Z" fill="var(--blue)"/><path d="M0 20 C70 -2 150 44 276 8" stroke="var(--grey)" stroke-width="2" fill="none"/></svg>
</section>
<p class="label" style="left:575px;top:436px">Letterhead Option 2</p>

<section class="piece envelope" style="top:18px;height:80px">
  <svg class="flap-line" viewBox="0 0 348 80" preserveAspectRatio="none"><path d="M0 0 L174 62 L348 0" stroke="#d6d8dc" stroke-width="1" fill="none"/></svg>
  <span class="center-mark" style="top:30px"></span>
</section>

<section class="piece envelope" style="top:106px;height:68px;background:var(--grey)">
  <svg class="flap-line" viewBox="0 0 348 68" preserveAspectRatio="none"><path d="M0 0 L348 0 L348 40 C240 60 110 60 0 40Z" fill="var(--grey-dark)"/></svg>
  <span class="center-mark" style="top:14px;background:var(--paper)"></span>
</section>

<section class="piece envelope" style="top:182px;height:48px;background:var(--blue)">
  <span class="center-mark" style="top:14px;background:var(--paper)"></span>
</section>

<section class="piece envelope" style="top:234px;height:56px">
  <svg class="flap-line" viewBox="0 0 348 56" preserveAspectRatio="none"><path d="M0 0 C120 30 228 30 348 0" stroke="#d6d8dc" stroke-width="1" fill="none"/></svg>
</section>

<section class="piece envelope env-front" style="top:300px;height:122px">
  <div class="brand"><span class="brand-mark"></span>KESTREL LEDGER</div>
  <div class="env-return">4826 N Halvern RD, STE 212<br>Tempe, AZ 85291</div>
  <svg class="wave" viewBox="0 0 348 40" preserveAspectRatio="none" height="40"><path d="M0 16 C90 2 190 34 348 8 L348 40 L0 40Z" fill="var(--blue)"/><path d="M0 11 C90 -3 190 29 348 3" stroke="var(--grey)" stroke-width="1.5" fill="none"/></svg>
</section>
<p class="label" style="left:975px;top:432px">Envelope Option 1</p>

</body>
</html>
```